Card for invoking rights with police

Our criminal defense law firm is seeking proposals for a design for our card intended for clients to carry with them in their car. Upon being pulled over, they would hand this card to the officer.
Text for the back of the card:
"For Law Enforcement:"
"I will comply with lawful orders but respectfully decline any test or other requests without my attorney. I wish to remain silent, do not consent to searches, and request to speak with my attorney now.
The back of the card should prominently feature the text and the firm logo should be secondary.
Front
Must prominently feature contact info: 503-555-0182. Do not include attorney name, email, phone from the example file. This is intended to be generic for the firm and not tied to an individual lawyer.
Included for design reference: current business card, firm logo.
We intend to use trenvo.com to produce the cards.
Updates
The back of the card should prominently display the text regarding invocation of rights. Please title it "For Law Enforcement".
Target Market(s)
People who have been stopped by police
Contact Information for Business Card
see project description
Look and feel

```html
<!DOCTYPE html>
<html lang="en">
<head>
<meta charset="utf-8">
<title>Harlow Law Firm – Rights Card</title>
<link rel="stylesheet" href="https://fonts.googleapis.com/css2?family=EB+Garamond:wght@400;600&family=Open+Sans:wght@400&display=swap">
<style>
  :root {
    --navy: #02345a;
    --ink: #141414;
    --paper: #ffffff;
    --backdrop: #222222;
    --serif: "EB Garamond", Georgia, serif;
    --sans: "Open Sans", Arial, sans-serif;
  }
  * { box-sizing: border-box; margin: 0; padding: 0; }
  html, body { width: 1200px; height: 780px; overflow: hidden; background: var(--backdrop); }
  .stage { position: relative; width: 1200px; height: 780px; }

  .card {
    position: absolute;
    width: 580px;
    height: 330px;
    overflow: hidden;
    box-shadow: 0 10px 24px rgba(0,0,0,.55);
  }

  /* Back of card */
  .card-back { left: 60px; top: 50px; background: var(--navy); color: var(--paper); text-align: center; }
  .card-back .firm-mark { margin-top: 62px; }
  .rights-title {
    margin-top: 40px;
    font-family: var(--serif);
    font-weight: 600;
    font-size: 21px;
    letter-spacing: .5px;
  }
  .rights-text {
    margin: 6px auto 0;
    width: 500px;
    font-family: var(--serif);
    font-size: 17.5px;
    line-height: 1.22;
  }

  /* Shared firm name lockup */
  .firm-mark {
    display: flex;
    align-items: center;
    justify-content: center;
    gap: 14px;
  }
  .firm-mark .mark-square { width: 30px; height: 30px; background: currentColor; }
  .firm-mark .firm-name {
    font-family: var(--serif);
    font-weight: 400;
    font-size: 30px;
    letter-spacing: 5px;
    text-transform: uppercase;
  }

  /* Front of card */
  .card-front { left: 560px; top: 410px; background: var(--paper); color: var(--ink); }
  .card-front .firm-mark { position: absolute; left: 60px; top: 50px; color: var(--navy); justify-content: flex-start; }
  .wave { position: absolute; inset: 0; }
  .address {
    position: absolute;
    right: 262px;
    top: 172px;
    font-family: var(--sans);
    font-style: normal;
    font-size: 13.5px;
    line-height: 1.35;
    text-align: right;
    white-space: nowrap;
  }
  .divider { position: absolute; left: 328px; top: 124px; width: 2px; height: 86px; background: var(--ink); }
  .contact-list {
    position: absolute;
    left: 344px;
    top: 124px;
    list-style: none;
    font-family: var(--sans);
    font-size: 13.5px;
    line-height: 1.45;
    white-space: nowrap;
  }
  .contact-list li { display: flex; align-items: center; gap: 6px; }
  .contact-list svg { width: 12px; height: 12px; fill: var(--ink); }
</style>
</head>
<body>
<main class="stage">

  <section class="card card-back" aria-label="Back of card">
    <div class="firm-mark">
      <span class="mark-square"></span>
      <span class="firm-name">Harlow Law Firm</span>
    </div>
    <h2 class="rights-title">FOR LAW ENFORCEMENT</h2>
    <p class="rights-text">I will comply with lawful orders but respectfully decline any test or other requests without my attorney. I wish to remain silent, do not consent to searches, and request to speak with my attorney now.</p>
  </section>

  <section class="card card-front" aria-label="Front of card">
    <svg class="wave" viewBox="0 0 580 330" preserveAspectRatio="none" aria-hidden="true">
      <path d="M0 296 C 220 296, 330 268, 410 238 C 480 212, 540 204, 580 200 L580 330 L0 330 Z" fill="var(--navy)"/>
      <path d="M0 308 C 225 307, 338 280, 418 250 C 488 224, 545 216, 580 213" fill="none" stroke="var(--paper)" stroke-width="3"/>
    </svg>

    <div class="firm-mark">
      <span class="mark-square"></span>
      <span class="firm-name">Harlow Law Firm</span>
    </div>

    <address class="address">
      2150 Lakeview Avenue NE<br>
      Suite 300 Fairmont, WA 98000
    </address>

    <div class="divider"></div>

    <ul class="contact-list">
      <li>
        <svg viewBox="0 0 12 12" aria-label="Phone"><path d="M1 3 Q6 0 11 3 L10 5 L8 4 L8 3 Q6 2 4 3 L4 4 L2 5 Z M3 6 H9 L10 11 H2 Z"/></svg>
        503.555.0182
      </li>
      <li>
        <svg viewBox="0 0 12 12" aria-label="Fax"><path d="M3 1 H9 V5 H3 Z M1 5 H11 V11 H1 Z"/></svg>
        503.555.0147
      </li>
      <li>
        <svg viewBox="0 0 12 12" aria-label="Website"><circle cx="6" cy="6" r="5.5"/></svg>
        www.harlowlawfirm.com
      </li>
    </ul>
  </section>

</main>
</body>
</html>
```